Marlow Ridgeway a PlateWork Fabricator! Pressure Vessels, Stainless Vessels, Steel Fabricator!

Update and modernize the www.marlowridgeway.example website. Basically throwing away the old site and coming back with a new feel, new look, but some of the same content. One of our other companies is www.keltonbuilders.example and if you view that site you will get a idea of how we would like the site to feel. Below are the MR logos and the colors are #231F20 and #6D0B17 and the font is Ethnocentric Rg.

Target Market(s)

Steel Fabrication, Platework, Vessel Fabrication,

Industry/Entity Type

Steel

Coding

Coded - Design and coding required

Number of Pages Required

5+ page

Font styles to use
Other font styles liked:
• Ethnocentric Rg

Requirements
Must have
• Industry feel... site must flow and color scheme and font be consistent.

```html
<!DOCTYPE html>
<html lang="en">
<head>
<meta charset="utf-8">
<title>Marlow Ridgeway — Plate Work Fabricator</title>
<link href="https://fonts.googleapis.com/css2?family=Oswald:wght@500;700&family=Open+Sans:wght@400;600;700&display=swap" rel="stylesheet">
<style>
:root{
  --ink:#231f20;
  --wine:#6d0b17;
  --red:#a3121f;
  --steel:#8d9196;
  --steel-light:#c9ccd0;
  --band:#a9adb1;
  --band-edge:#6e7276;
  --paper:#ffffff;
  --text:#555;
  --footer:#1b1819;
}
*{box-sizing:border-box;margin:0;padding:0}
html,body{width:716px;height:1200px;overflow:hidden}
body{font-family:"Open Sans",Arial,sans-serif;color:var(--text);background:var(--paper);font-size:7px;line-height:1.5}
h2,h3,.btn,.nav a,.brand-name{font-family:"Oswald","Arial Narrow",sans-serif;text-transform:uppercase}

.site-header{height:42px;background:var(--ink);display:flex;align-items:center;justify-content:space-between;padding:0 70px 0 62px}
.brand{display:flex;align-items:center;gap:7px}
.brand-dot{width:24px;height:24px;border-radius:50%;background:var(--wine)}
.brand-name{color:#fff;font-size:14px;font-weight:700;letter-spacing:.5px}
.nav{display:flex;height:42px}
.nav a{color:#ddd;text-decoration:none;font-size:7px;font-weight:500;padding:0 10px;display:flex;align-items:center;letter-spacing:.4px}
.nav a.active{background:var(--red);color:#fff}

.hero{height:240px;background:linear-gradient(180deg,#7a6a58 0%,#c8a57a 30%,#e3d2b4 55%,#b7b8b4 75%,#6f7072 100%)}
.divider{height:13px;background:var(--band);border-top:1px solid var(--band-edge);border-bottom:1px solid var(--band-edge)}

.services{height:277px;padding:24px 62px 0}
.section-title{font-size:13px;color:var(--ink);font-weight:700;letter-spacing:.6px}
.cards{display:grid;grid-template-columns:repeat(4,1fr);gap:12px;margin-top:16px}
.card-media{height:113px;position:relative}
.card-tag{position:absolute;top:0;left:0;right:22px;background:var(--red);color:#fff;font-size:7px;font-weight:600;padding:3px 6px}
.m1{background:linear-gradient(160deg,#2b2b30,#6d4a3a 50%,#b9552b)}
.m2{background:linear-gradient(160deg,#e9e6e0,#9fa0a2 60%,#5d5f61)}
.m3{background:linear-gradient(160deg,#d9d2c3,#b4a68a 55%,#7c705c)}
.m4{background:linear-gradient(160deg,#3c4148,#6b6f76 50%,#b3432e)}
.card p{margin-top:8px;font-size:6px;line-height:1.55;height:46px}
.btn{display:inline-block;background:var(--ink);color:#fff;font-size:6.5px;font-weight:500;padding:4px 8px;letter-spacing:.4px;margin-top:8px}
.btn.red{background:var(--red)}

.testimonials{height:203px;background:linear-gradient(180deg,#4a423c,#7b6e63 45%,#9a8b7c 70%,#5a4f46);position:relative;text-align:center;padding-top:36px}
.testimonials .section-title{color:#fff}
.quote-box{position:absolute;left:195px;width:326px;top:72px;height:103px;background:rgba(109,11,23,.88);color:#f1e6e6;font-size:6.5px;padding:14px 22px;line-height:1.7}

.features{height:195px;display:grid;grid-template-columns:1fr 1fr;gap:34px;padding:28px 62px 0}
.features p{font-size:6px;margin-top:8px;line-height:1.6}
.badges{display:flex;gap:14px;margin-top:10px;align-items:center}
.badge{width:34px;height:22px;background:var(--steel-light)}
.badge.round{border-radius:50%;width:24px;height:24px;background:var(--steel)}
.badge.wine{background:var(--wine)}

.call-bar{height:23px;background:var(--ink);display:flex;align-items:center;justify-content:space-between;padding:0 62px}
.call{background:var(--red);color:#fff;font-family:"Oswald",sans-serif;font-size:9px;padding:0 12px;height:23px;display:flex;align-items:center;gap:6px}
.social{display:flex;gap:4px}
.social span{width:11px;height:11px;border-radius:50%;background:var(--red)}

.site-footer{height:179px;background:var(--footer);display:grid;grid-template-columns:1.1fr .6fr .6fr 1.3fr;gap:18px;padding:18px 62px 0;color:#b8b4b4}
.site-footer h3{color:var(--red);font-size:8px;font-weight:700;letter-spacing:.4px;margin-bottom:8px}
.site-footer p,.site-footer li{font-size:6px;line-height:1.7;list-style:none}
.quote-form{display:grid;grid-template-columns:1fr 1fr;gap:4px}
.field{height:11px;background:#fff;font-size:5.5px;color:#999;padding:2px 4px}
.field.wide{grid-column:1/3;height:26px}
.quote-form .btn{grid-column:2;margin:2px 0 0;text-align:center;background:var(--red)}

.legal{height:18px;background:#111;color:#888;font-size:5.5px;display:flex;align-items:center;padding:0 62px}
</style>
</head>
<body>
<header class="site-header">
  <div class="brand"><span class="brand-dot"></span><span class="brand-name">Marlow Ridgeway</span></div>
  <nav class="nav">
    <a class="active">Home</a><a>About</a><a>Products</a><a>Services</a><a>What We Do</a><a>Resources</a><a>Contact</a>
  </nav>
</header>

<section class="hero" role="img" aria-label="Row of large steel storage silos under a warm sky"></section>
<div class="divider"></div>

<section class="services">
  <h2 class="section-title">Marlow Ridgeway Services</h2>
  <div class="cards">
    <article class="card">
      <div class="card-media m1" role="img" aria-label="Welder treating a seam with glowing heat"><span class="card-tag">Post Weld Heat Treatment</span></div>
      <p>Post weld heat treatment relieves stress in finished vessels, improving strength and service life for every fabricated part we ship.</p>
      <span class="btn">Read More</span>
    </article>
    <article class="card">
      <div class="card-media m2" role="img" aria-label="Drilling machine boring a steel plate"><span class="card-tag">Drilling and Boring</span></div>
      <p>Our drilling and boring crew delivers precise holes and bores in heavy plate, flanges and shells to tight shop tolerances.</p>
      <span class="btn">Read More</span>
    </article>
    <article class="card">
      <div class="card-media m3" role="img" aria-label="Coated steel tanks in the yard"><span class="card-tag">Coatings</span></div>
      <p>Protective coatings shield tanks and vessels from weather and corrosion, applied in house to match each project spec.</p>
      <span class="btn">Read More</span>
    </article>
    <article class="card">
      <div class="card-media m4" role="img" aria-label="Technician testing a weld"><span class="card-tag">Non Destructive Testing</span></div>
      <p>Non destructive testing confirms weld quality with ultrasonic, radiographic and dye checks before any vessel leaves.</p>
      <span class="btn">Read More</span>
    </article>
  </div>
</section>
<div class="divider"></div>

<section class="testimonials" role="img" aria-label="Large tank section loaded on a trailer outdoors">
  <h2 class="section-title">What Our Customers Say</h2>
  <blockquote class="quote-box">We have hired Marlow Ridgeway for many years on jobs large and small. Their crew is skilled, the shop runs on time, and the finished work is always clean. We trust them with our toughest vessel builds and would gladly recommend their team to anyone in the industry.</blockquote>
</section>
<div class="divider"></div>

<section class="features">
  <div>
    <h2 class="section-title">Success at Any Size</h2>
    <p>Marlow Ridgeway builds everything from small process tanks to large pressure vessels. Our plate shop handles heavy rolling, forming and welding, so customers get one partner for the full job from design review to final delivery on site.</p>
    <span class="btn">Learn More</span>
  </div>
  <div>
    <h2 class="section-title">Quality Assurance Guaranteed</h2>
    <p>Every vessel passes a documented quality program. Certified welders, inspectors and engineers check each step so the finished product meets code and the client's own standards.</p>
    <div class="badges"><span class="badge round"></span><span class="badge"></span><span class="badge wine"></span><span class="badge"></span></div>
    <span class="btn red">Products</span> <span class="btn">Services</span>
  </div>
</section>

<div class="call-bar">
  <div class="call">
    <svg width="9" height="9" viewBox="0 0 24 24" fill="#fff" aria-hidden="true"><path d="M6.6 10.8a15 15 0 0 0 6.6 6.6l2.2-2.2a1 1 0 0 1 1-.25 11.4 11.4 0 0 0 3.6.57 1 1 0 0 1 1 1V20a1 1 0 0 1-1 1A17 17 0 0 1 3 4a1 1 0 0 1 1-1h3.5a1 1 0 0 1 1 1c0 1.25.2 2.45.57 3.57a1 1 0 0 1-.25 1z"/></svg>
    Call Us Now: (555) 014-2290
  </div>
  <div class="social"><span></span><span></span><span></span><span></span></div>
</div>

<footer class="site-footer">
  <div>
    <h3>About Us</h3>
    <p>Founded as a family run plate shop, Marlow Ridgeway has grown into a trusted fabricator of pressure vessels, stainless tanks and heavy steel parts serving industrial clients across the region with a wide range of products.</p>
  </div>
  <div>
    <h3>Navigation</h3>
    <ul><li>Home</li><li>About Us</li><li>Products</li><li>Services</li><li>What We Do</li></ul>
  </div>
  <div>
    <h3>&nbsp;</h3>
    <ul><li>Resources</li><li>Contact</li><li>Careers</li></ul>
  </div>
  <div>
    <h3>Request a Quote</h3>
    <form class="quote-form">
      <span class="field">Name</span><span class="field">Email</span>
      <span class="field">Phone</span><span class="field">Company</span>
      <span class="field wide">Describe your project</span>
      <span class="btn">Submit Your Quote</span>
    </form>
  </div>
</footer>
<div class="legal">Copyright © Marlow Ridgeway. All Rights Reserved.</div>
</body>
</html>
```